Retail Sign for Houseplant Campaign

Sign will measure 3 to 4 foot tall by 22.2inches and place on rolling racks of houseplants for a retail promotion in The Yardwell Mart. The theme of the promotion will be "New Year, New You!" Selling points which should be on the sign are Houseplants give you a taste of nature, Houseplants boost air quality inside your home, Indoor plants reduce anxiety, Indoor plants make you more productive, Houseplants improve your concentration and memory.
Updates

Target Market(s)

People who love plants

Industry/Entity Type

Horticulture/ retail

Colors
00AB8E
00BBA5
67D7C9
C6EFE9
E9F9F6
59FF00
82FF00
B8FF75
E3FFCB
F4FFEA
FFF300
FFF600
FEFA6F
FFFEC7
FFFEE8

Requirements
Must have
• Must feel energetic and encourage people to buy plants. Should include 1-2 photos and the selling points listed

```html
<!DOCTYPE html>
<html lang="en">
<head>
<meta charset="utf-8">
<title>New Year, New You – Houseplant Sign</title>
<link href="https://fonts.googleapis.com/css2?family=Oswald:wght@500;600&family=Poppins:wght@500;700&display=swap" rel="stylesheet">
<style>
  :root {
    --backdrop: #b7c4a3;
    --paper: #ffffff;
    --leaf-green: #6cc04a;
    --forest: #45682f;
    --frame-green: #4a8a35;
    --lime: #d2dc28;
    --sun-yellow: #f2e600;
    --pale-yellow: #eef3b9;
    --pale-green: #d9ebc4;
    --ink: #111111;
  }
  * { box-sizing: border-box; margin: 0; padding: 0; }
  html, body {
    width: 1200px; height: 1200px; overflow: hidden;
    background: var(--backdrop);
  }
  .sign {
    position: absolute; left: 250px; top: 41px;
    width: 700px; height: 1118px;
    background: var(--paper);
    overflow: hidden;
  }
  .blob { position: absolute; }
  .headline {
    position: absolute; left: 0; right: 0; top: 26px;
    text-align: center; padding-left: 18px;
    font-family: "Oswald", sans-serif; font-weight: 500;
    font-size: 76px; line-height: 1; letter-spacing: -1px;
    color: var(--leaf-green);
  }
  .hero-band {
    position: absolute; left: 0; top: 143px; width: 581px; height: 387px;
    background: var(--forest);
  }
  .hero-photo {
    position: absolute; left: 190px; top: 179px; width: 456px; height: 315px;
    border: 8px solid var(--sun-yellow);
    background: linear-gradient(160deg, #f3f3f1 0%, #e6e4df 45%, #cfd6c4 70%, #9aa6b8 100%);
  }
  .facts-title {
    position: absolute; left: 33px; top: 550px;
    font-family: "Oswald", sans-serif; font-weight: 600;
    font-size: 45px; line-height: 1; letter-spacing: -1px;
    color: var(--leaf-green);
  }
  .facts {
    position: absolute; left: 45px; top: 603px;
    list-style: none;
    font-family: "Poppins", sans-serif; font-weight: 700;
    font-size: 20px; line-height: 31px; text-transform: uppercase;
    color: var(--ink); white-space: nowrap;
  }
  .facts li::before { content: "• "; }
  .promo-band {
    position: absolute; left: 187px; top: 781px; width: 513px; height: 337px;
    background: var(--lime);
  }
  .promo-photo {
    position: absolute; left: 340px; top: 823px; width: 277px; height: 272px;
    border: 5px solid var(--frame-green);
    background: linear-gradient(120deg, #f1efec 0%, #e9e3dc 55%, #c9a98d 100%);
  }
  .grower-name {
    position: absolute; left: 24px; top: 952px;
    font-family: "Poppins", sans-serif; font-weight: 500;
    font-size: 15px; line-height: 1.2; letter-spacing: 1px;
    color: var(--forest);
  }
  .store {
    position: absolute; left: 24px; top: 1010px;
    display: flex; align-items: center; gap: 8px;
  }
  .store-dot { width: 16px; height: 16px; border-radius: 50%; background: var(--forest); }
  .store-name {
    font-family: "Poppins", sans-serif; font-weight: 500;
    font-size: 15px; line-height: 1.2; color: var(--forest);
  }
</style>
</head>
<body>
  <main class="sign">
    <svg class="blob" style="left:0;top:5px" width="36" height="135" viewBox="0 0 36 135"><path d="M0 0 C20 20 40 70 24 105 C18 120 8 130 0 135 Z" fill="var(--pale-yellow)"/></svg>
    <svg class="blob" style="left:672px;top:0" width="28" height="30" viewBox="0 0 28 30"><path d="M28 0 V30 C12 30 0 20 4 0 Z" fill="var(--pale-green)"/></svg>

    <h1 class="headline">NEW YEAR, NEW YOU</h1>

    <div class="hero-band"></div>
    <div class="hero-photo" role="img" aria-label="Photo of a woman relaxing on the floor of a bright living room surrounded by houseplants"></div>

    <h2 class="facts-title">DID YOU KNOW?</h2>

    <svg class="blob" style="left:34px;top:684px" width="165" height="80" viewBox="0 0 165 80"><path d="M10 20 C30 -5 90 0 130 25 C170 50 150 80 110 78 C60 76 -10 50 10 20 Z" fill="var(--pale-green)"/></svg>
    <svg class="blob" style="left:580px;top:612px" width="100" height="115" viewBox="0 0 100 115"><path d="M30 10 C55 -10 95 10 98 50 C100 95 70 120 40 105 C10 90 0 35 30 10 Z" fill="var(--pale-yellow)"/></svg>

    <ul class="facts">
      <li>Houseplants give you a taste of nature</li>
      <li>Houseplants improve your concentration &amp; memory</li>
      <li>Houseplants boost air quality inside your home</li>
      <li>Indoor plants make you more productive</li>
      <li>Indoor plants reduce anxiety</li>
    </ul>

    <svg class="blob" style="left:0;top:817px" width="60" height="82" viewBox="0 0 60 82"><path d="M0 10 C20 -5 55 0 58 25 C60 45 25 70 0 82 Z" fill="var(--pale-yellow)"/></svg>
    <svg class="blob" style="left:0;top:1080px" width="30" height="38" viewBox="0 0 30 38"><path d="M0 0 C15 10 30 25 30 38 H0 Z" fill="var(--pale-green)"/></svg>

    <div class="promo-band"></div>
    <div class="promo-photo" role="img" aria-label="Photo of a smiling woman holding a potted croton plant in a woven basket"></div>

    <p class="grower-name">LEAFLINE GROWERS</p>
    <div class="store">
      <span class="store-dot"></span>
      <span class="store-name">The Yardwell Mart</span>
    </div>
  </main>
</body>
</html>
```